Web Design with a Twist! Not cheap design

Please note that this project is ending at 5pm on Tuesday the 28th of September, Australian Western Standard Time!!

Please also note that this project has now been guaranteed!

This project involves three primary elements:
* Logo design;
* Web design - of additional pages and page elements to fit into a site that is already in design/development;
* Graphic design - various images used on the site.

The following materials are included for the project:
* Project requirements
* Company / Site name
* Company / Site description
* Wireframes for new pages / page elements
* Screenshots of existing designs and accompanying definition of constraints for new designs
* PSDs for existing site designs
* Technical requirements for designs
* Content (to guide designs)

Project Requirements:

* Logo design:
This is a new company / site, so we need a new logo. We want to see what you come up with here without giving too much direction that may restrict creativity. If desired, you may find possible guidance through considering the company name, company description, and the existing site designs. Please note that the current logo in the site is for placeholder purposes only.

* Web design:
We need the following pages (and features) to be designed for the site:
• Home page
• Advertise page
• How it works page
We’ve provided some wireframes for the pages, however we definitely don't want you to be guided by the layout/styling at all - the wireframes are only there to indicate the features that we require on each page only. So please ignore all aspects of the wireframes except for the indications of features and functionality.

* Graphic design:
We need various images to be designed throughout the site. These include:
• The image at the top of the ‘Home’ page – please note we will provide some direction on this asap
• The image at the top of the ‘Advertise’ page – please note we will provide some direction n this asap
• The image at the top of the ‘How it Works’ pages
• The images that accompany each of the left hand menu items on the ‘How it Works’ pages (the main images & thumbnails if that’s part of your design). Please note that these images need to be constructed to match the Headlines for each of the ‘What’, ‘Who’, ‘Where’, etc menu items. These Headlines (and some descriptive text) can be found in the Content section at the end of this brief.
• The map of Australia for the ‘Home’ page
• The images to accompany the pricing section of the ‘Advertise’ page
• The variations of the ‘Life in the search lane’ images that are used on the ‘Home’, ‘Advertise’, and ‘How it Works’ pages. Please note that if you want to use different imagery (or no imagery, dependent upon your design) for the Home and Advertise pages then this is your call.

Company Name:
TaskBloom

Company / Site description:
This site will provide a means for contractors ('advertisers') to easily specify and advertise their services, coupled with a means for employers (‘buyers’) to easily seek out and contact these people.
The site will cater for contractor-side advertisements only; job postings will not be accommodated (turning the traditional job advertisement model on its head).
In general, the functionality of the site is somewhat like a mashup of sites like crewvault.com and stayvane.com. The site will incorporate the following primary features of contractor profile display and search, company profile display, (and an availability calendar for v2 release).

Constraints for designs:
On some of the existing designs you will notice that a number of the elements of the site have already been designed. When constructing your designs, please work in accordance with the following constraints:

You have to keep:
• Colour scheme in the header
• Colour scheme in the top navigation buttons (including text colour and background colour)
• Colour scheme for the buttons like on the Register page

You can ignore:
• The existing placeholder logo
• Border, layout, and colour scheme for page elements (like the lines around and inside the register section on the Register page)
• Design of text fields
• Font colour scheme throughout the site – the orange and grey headlines and body text
• Design and colour scheme of the map of Australia
• The breadcrumbs (whether or not they appear, and their layout, styling, colour scheme etc)
• Dropdown styling (assuming you had to make some; currently not on any pages we’re asking you to do) like on the Browse Profession page
• Profile styling (for the home page featured profiles) like on the Browse Profession page
• Footer styling
• Anything else we haven’t explicitly asked you to keep

Technical requirements for design:
Any site designs in either Layered PixelForge files (PSD's) or Illustrator Drawings (AI). RGB Color. Must fit current site design, we work to 1024 wide screens. Usuable area is defined in site designs that are attached in the PixelForge documents; it's around 960px.
Logo work needs to be Illustrator Drawings (AI) and EPS. Need CMYK images for printing and RGB for screen. Logos must include any special fonts that are used as TTF or Open Type. Logos need Color, Monochrome, Reversed and both Tall and Wide usages.

Content for the 'How it Works' pages - this content should guide the images that appear on each page.
* What
Headline: TaskBloom brings contractors and employers together
Descriptive text: (turns the traditional job search model on its head)
* Who
Headline: TaskBloom is for highly skilled professionals and fast moving companies
Descriptive text:
* Where
Headline: Anywhere in Australia, TaskBloom is working by your side
Descriptive text:
* Why
Headline: There are more than 1 million reasons to love TaskBloom
Descriptive text: In Australia, there are 1 million people who work as contractors in their main job, and a further 100,000 people who are contractors in their second job. That’s a lot of contractors!
* When
Headline: TaskBloom is forming partnerships 24 hours a day
Descriptive text:
* How
Headline: Life in the search lane, with TaskBloom
Descriptive text: Advertise on TaskBloom now, and get your life in the search lane.

Remember
Just remember the wireframes we have submitted are just a guide – we want to see your creativity shine. And above all else - have fun!
Thank you.
Updates

Please note the deadline for this design competition 5pm on Tuesday the 28th of September, Australian Western Standard Time.

Just under 3 days away!

The deadline of the project will soon be updated to reflect this.

Hi Designers!

Just to be 100% clear about the deadline - the timer is currently showing 7 hours too many. In other words, the project will end 7 hours before the timer finishes.

I will send a notification if the timer starts to display the correct time. So until then, please remember that the deadline is earlier than it seems!

Thanks

Hi Designers,

A couple of really important points:

Firstly - if everyone could please stick to the theme that we provided in the PixelForge files that would be excellent. It is not possible for us to create a new theme. We're dealing with very tight deadlines, so please just provide designs that fit within the current theme.

Secondly, we were really hoping for more illustrations / graphics to be provided in the designs. We're not a fan of the stock photos of generic business people. So please send through designs that incorporate illustrations / graphics for any imagery.

Also just a reminder that this competition is still ending 7 hours earlier than the timer currently displays.

Thanks.

Target Market(s)

The ‘advertiser’ target market for the site is white collar professionals, in all types of industries. The site will be catering for premium contractors only. The site will be catering for both 'in person' contractors, as well as 'knowledge economy' contractors. The site will not be seeking to compete with gigmora.com, plixo.com, taskrune.com, or similar sites.

The advertiser target market will also encompass companies and labour hire agencies that have contractors in their workforce.

The ‘buyer’ target market will encompass employers, recruitment agents, and member-to-member hiring.

Industry/Entity Type

Contractor

Requirements
Must have
• As per overview
Nice to have
• As per overview
Should not have
• As per overview

```html
<!DOCTYPE html>
<html lang="en">
<head>
<meta charset="utf-8">
<title>TaskBloom – Contractors and Employers Together</title>
<link rel="stylesheet" href="https://fonts.googleapis.com/css2?family=Arimo:wght@400;700&family=Roboto+Condensed:wght@700&display=swap">
<style>
:root{
  --page:#f2f2f2;
  --white:#ffffff;
  --orange:#ff6a0d;
  --ink:#2f3b4a;
  --body:#4d5866;
  --line:#d6d9dc;
  --strip:#e6e6e6;
  --panel-tint:#e8eff1;
  --teal-tint:#cfe6e9;
  --footer:#434c56;
  --footer-text:#8f99a3;
  --footer-head:#b9c2cb;
  --red:#b8241a;
}
*{box-sizing:border-box;margin:0;padding:0}
html,body{width:1200px;height:1054px;overflow:hidden}
body{background:var(--page);font-family:"Arimo",Arial,sans-serif;color:var(--body);position:relative}
.abs{position:absolute}

.account-links{left:898px;top:12px;font-size:11px;letter-spacing:.5px;color:#7b8a99}
.account-links span{margin:0 6px;color:#a5afb9}

.nav-band{left:0;top:54px;width:1200px;height:45px;background:linear-gradient(#71849a,#56697d);border-bottom:1px solid #4a5b6c}
.nav-link{top:71px;font-size:12.5px;letter-spacing:.3px;color:#b6c2ce;text-decoration:none}
.nav-link.current{color:#fff}

.site-search{left:852px;top:66px;width:191px;height:25px;display:flex;border-radius:3px;overflow:hidden;box-shadow:0 0 0 1px #8394a5}
.site-search .field{flex:1;background:#fff;font-size:12px;color:#9aa3ac;padding:6px 0 0 30px;position:relative}
.site-search .field svg{position:absolute;left:11px;top:7px}
.site-search .go{width:32px;background:linear-gradient(#9aa9b8,#7e8fa0);color:#fff;font-size:13px;font-weight:700;text-align:center;line-height:25px}

.hero{left:113px;top:98px;width:950px;height:385px;background:var(--white);border:1px solid var(--line);border-top:none;border-radius:0 0 6px 6px}

.brand{left:146px;top:16px;display:flex;align-items:center;gap:9px}
.brand-mark{width:18px;height:18px;background:var(--orange)}
.brand-name{font-weight:700;font-size:22px;color:var(--orange);letter-spacing:.2px}

.hero-title{left:147px;top:193px;font-family:"Roboto Condensed",Arial,sans-serif;font-weight:700;font-size:30px;color:var(--ink);letter-spacing:-.4px}
.hero-title em{font-style:normal;color:var(--orange)}
.hero-copy{left:150px;top:240px;width:480px;font-size:14.5px;line-height:22px;color:#566272}
.hero-copy strong{color:#3e4a57}
.btn-register{left:311px;top:326px;width:114px;height:30px;border-radius:15px;background:linear-gradient(#fbfbfb,#d7d7d7);box-shadow:0 0 0 1px #c9c9c9,0 1px 2px rgba(0,0,0,.2);font-weight:700;font-size:13px;color:#3b4650;text-align:center;line-height:30px}
.map{left:688px;top:132px;width:352px;height:262px;background:radial-gradient(ellipse at 55% 50%,#e2e4e6 0%,#eaebec 60%,#fff 78%)}

.finder{left:120px;top:405px;width:931px;height:68px;background:var(--strip)}
.finder-figure{left:136px;top:406px;width:56px;height:64px;background:linear-gradient(#8b8f94,#3a3f45 55%,#2a2d31);border-radius:22px 22px 4px 4px}
.finder-title{left:205px;top:430px;font-size:17.5px;font-weight:700;color:var(--ink);letter-spacing:-.1px}
.input{height:27px;background:#fff;border:1px solid #cfd3d6;font-size:12px;color:#9aa2aa;padding:5px 0 0 11px}
.kw{left:503px;top:427px;width:183px}
.state{left:698px;top:428px;width:152px}
.state .arrow{position:absolute;right:3px;top:4px;width:17px;height:17px;border:1px solid #b4b9be;background:#f5f5f5}
.btn-orange{height:28px;border-radius:3px;background:linear-gradient(#ff7a50,#ee5630);color:#fff;font-weight:700;font-size:13.5px;text-align:center;line-height:28px;box-shadow:0 1px 1px rgba(0,0,0,.25)}

.panel-head{height:36px;background:linear-gradient(#6a7b8d,#46566a);border-radius:5px 5px 0 0;color:#fff;font-weight:700;font-size:16.5px;line-height:34px;padding-left:31px;text-shadow:0 1px 1px rgba(0,0,0,.4)}
.about{left:114px;top:489px;width:622px;height:341px;border:1px solid #c5cbd0;border-radius:5px 5px 0 0;background:linear-gradient(#f7f9fa,#e7eef1 30%,#fafbfb 60%,#fff)}
.about-body{padding:20px 0 0 35px;font-size:11px;line-height:20px;color:#4a5563}
.about-body h3{font-size:12.5px;color:#2f3b48;margin-bottom:1px}
.points{list-style:none;margin-top:14px}
.points li{position:relative;padding-left:57px;margin-bottom:14px}
.points li svg{position:absolute;left:26px;top:7px}
.points h4{font-size:12.5px;color:#2f3b48;line-height:16px;margin-bottom:3px}
.read-more{position:absolute;right:19px;bottom:8px;font-size:11.5px;font-weight:700;color:var(--red)}

.how{left:115px;top:839px;width:620px;height:56px;background:var(--teal-tint);border:1px solid #a9c3c8;border-radius:2px}
.how-icon{left:131px;top:849px;width:52px;height:36px}
.how-title{left:201px;top:853px;font-weight:700;font-size:19.5px;color:var(--ink);letter-spacing:-.3px}
.how-title span{color:var(--red)}

.featured{left:746px;top:489px;width:318px;height:406px;border:1px solid #c5cbd0;border-radius:5px 5px 0 0;background:var(--panel-tint)}
.profile{position:absolute;left:0;width:316px;border-bottom:1px solid #cfd8dc}
.photo{position:absolute;left:13px;width:76px;height:81px;border:3px solid #fff;box-shadow:0 0 0 1px #b9c2c8;background:linear-gradient(#e7ecef,#b9c6cf)}
.profile .name{position:absolute;left:98px;font-size:12.5px;color:var(--orange)}
.profile .role{position:absolute;left:99px;font-size:13.5px;font-weight:700;color:#3c4856}
.profile .skills{position:absolute;left:100px;width:200px;font-size:11px;line-height:13px;color:#4e5966}

.footer{left:0;top:938px;width:1200px;height:116px;background:var(--footer);box-shadow:0 -4px 6px rgba(0,0,0,.15) inset}
.footer-col{top:956px;font-size:12px;line-height:20px;color:var(--footer-text);letter-spacing:.3px}
.footer-col h5{font-size:12px;color:var(--footer-head);line-height:16px;margin-bottom:4px}
.follow{left:841px;top:967px;font-size:12px;font-weight:700;color:var(--footer-text)}
.social{top:966px;width:15px;height:15px;border-radius:2px;background:#5f86b8}
.copyright{left:795px;top:1000px;font-size:11.5px;color:var(--footer-text)}
</style>
</head>
<body>

<div class="abs account-links">LOGIN<span>|</span>RESIGTER NOW</div>

<div class="abs brand"><span class="brand-mark"></span><span class="brand-name">TaskBloom</span></div>

<div class="abs nav-band"></div>
<nav>
  <a class="abs nav-link current" style="left:340px" href="#">HOME</a>
  <a class="abs nav-link" style="left:429px" href="#">FIND</a>
  <a class="abs nav-link" style="left:507px" href="#">ADVERTISE</a>
  <a class="abs nav-link" style="left:627px" href="#">HOW IT WORKS</a>
  <a class="abs nav-link" style="left:771px" href="#">BLOG</a>
</nav>

<div class="abs site-search">
  <div class="field">
    <svg width="10" height="10" viewBox="0 0 10 10"><circle cx="4" cy="4" r="3" fill="none" stroke="#9aa3ac" stroke-width="1.3"/><line x1="6.3" y1="6.3" x2="9.3" y2="9.3" stroke="#9aa3ac" stroke-width="1.5"/></svg>
    Find Contrator
  </div>
  <div class="go">Go</div>
</div>

<section class="abs hero"></section>

<h1 class="abs hero-title">We brings <em>contractors</em> &amp; <em>employers</em> together</h1>
<p class="abs hero-copy"><strong>TASKBLOOM</strong> will provide a means for contractors ('advertisers') to easily specify and advertise their services, coupled with a means for employers (‘buyers’) to easily seek out and contact these people.</p>
<div class="abs btn-register">Resigter Now!</div>

<div class="abs map" role="img" aria-label="Map of Australia with orange pins on each state and territory"></div>

<div class="abs finder"></div>
<div class="abs finder-figure" role="img" aria-label="Illustrated professional in a dark suit"></div>
<div class="abs finder-title">Find Highly Skilled Professionals</div>
<div class="abs input kw">Type Keywords</div>
<div class="abs input state">Select State
  <span class="arrow"><svg width="15" height="15" viewBox="0 0 15 15"><path d="M4.5 6h6l-3 3.5z" fill="#555"/></svg></span>
</div>
<div class="abs btn-orange" style="left:877px;top:428px;width:144px">Find Contractors</div>

<section class="abs about">
  <div class="panel-head">About TaskBloom</div>
  <div class="about-body">
    <h3>Sed gravida commodo lacus sed faucibus.</h3>
    <p>Donec et nibh mauris. In lobortis massa quis nibh varius at euismod risus eleifend. Maecenas id mi ante. Morbi<br>adipiscing molestie convallis. Morbi est metus, porttitor quis fermentum laoreet, aliquam ut arcu.<br>Curabitur eget lacus at nisl bibendum hendrerit ac nec nulla. Pellentesque at elit eu leo mattis eleifend quis ac urna.</p>
    <ul class="points">
      <li><svg width="18" height="14" viewBox="0 0 18 14"><path d="M1 7l5 5L17 1" fill="none" stroke="#e2641c" stroke-width="3"/></svg>
        <h4>Sed gravida commodo lacus sed faucibus.</h4>Donec et nibh mauris. In lobortis massa quis nibh varius at euismod risus eleifend.</li>
      <li><svg width="18" height="14" viewBox="0 0 18 14"><path d="M1 7l5 5L17 1" fill="none" stroke="#e2641c" stroke-width="3"/></svg>
        <h4>Sed gravida commodo lacus sed faucibus.</h4>Donec et nibh mauris. In lobortis massa quis nibh varius at euismod risus eleifend. Donec et nibh mauris.<br>In lobortis massa quis nibh varius at euismod risus eleifend.</li>
      <li style="padding-left:55px"><svg width="18" height="14" viewBox="0 0 18 14"><path d="M1 7l5 5L17 1" fill="none" stroke="#e2641c" stroke-width="3"/></svg>
        <h4>Sed gravida commodo lacus sed faucibus.</h4>Donec et nibh mauris. In lobortis massa quis nibh varius at euismod risus eleifend.</li>
    </ul>
  </div>
  <div class="read-more">Read More »</div>
</section>

<div class="abs how"></div>
<svg class="abs how-icon" viewBox="0 0 52 36" aria-hidden="true">
  <path d="M2 1h38v23l10 10-14-6H2z" fill="#f4f7f8" stroke="#8a99a6"/>
  <text x="21" y="23" text-anchor="middle" font-family="Arimo,sans-serif" font-weight="700" font-size="20" fill="#3b4754">?</text>
</svg>
<div class="abs how-title">How it Works - “<span>Life in the Search Lane?</span>”</div>

<section class="abs featured">
  <div class="panel-head">Featured Profile</div>
  <article class="profile" style="top:36px;height:108px">
    <div class="photo" style="top:13px" role="img" aria-label="Profile photo of Marcus Delacroix"></div>
    <div class="name" style="top:14px">Marcus Delacroix</div>
    <div class="role" style="top:32px">Designer, Developer, Producer</div>
    <div class="skills" style="top:53px">QueryKit, PixelForge, WebStack, Project Management, Editorial, Photography, Consultancy</div>
  </article>
  <article class="profile" style="top:144px;height:108px">
    <div class="photo" style="top:13px" role="img" aria-label="Profile photo of Owen Pratley"></div>
    <div class="name" style="top:15px">Owen Pratley</div>
    <div class="role" style="top:33px">Consultant, Developer</div>
    <div class="skills" style="top:54px">QueryKit, PixelForge, WebStack, Project Management</div>
  </article>
  <article class="profile" style="top:252px;height:152px;border-bottom:none">
    <div class="photo" style="top:17px" role="img" aria-label="Profile photo of Glen Harrow"></div>
    <div class="name" style="top:19px">Glen Harrow</div>
    <div class="role" style="top:37px">Designer, Developer, Producer</div>
    <div class="skills" style="top:58px">Servicing New South Wales, Victoria and New South Wales</div>
    <div class="btn-orange" style="position:absolute;left:146px;top:110px;width:144px">Find Contractors</div>
  </article>
</section>

<footer class="abs footer"></footer>
<div class="abs footer-col" style="left:137px"><h5>About us</h5>Features<br>Pricing<br>Team</div>
<div class="abs footer-col" style="left:249px"><h5>Support</h5>Contact us<br>FAQ</div>
<div class="abs footer-col" style="left:360px"><h5>Browse</h5>By state<br>Business</div>
<div class="abs footer-col" style="left:468px"><h5>Legal</h5>Privacy Policy<br>Terms &amp; Conditions</div>
<div class="abs follow">Follow us on:</div>
<div class="abs social" style="left:929px" aria-label="Social profile"></div>
<div class="abs social" style="left:951px" aria-label="Social profile"></div>
<div class="abs social" style="left:973px;background:#6fb2dd" aria-label="Social profile"></div>
<div class="abs copyright">© Copyright 2010 TaskBloom.Al right reserved.</div>

</body>
</html>
```